Jewelery Website

Please visit: http://www.kelidunmore.example/dev/wpnew/

Target Market(s)

Women between 25 and 44 years old

Number of Pages Required

5+ page

Font styles to use
Sans Serif
Script
Other font styles liked:
• Futura

Colors

Designer to choose colors to be used in the design.

```html
<!DOCTYPE html>
<html lang="en">
<head>
<meta charset="utf-8">
<title>Keli Dunmore Pearls</title>
<link href="https://fonts.googleapis.com/css2?family=Jost:wght@300;400&display=swap" rel="stylesheet">
<style>
  :root {
    --ink: #2f2f2f;
    --white: #ffffff;
    --menu-bg: #f3f7fa;
    --menu-active: #e1e6e9;
    --skin: #d7a49a;
    --skin-soft: #e6c3ba;
    --lace: #f1ecef;
    --teal: #1f4a57;
    --teal-light: #4f8ea0;
    --pearl-grey: #8b8590;
    --deep: #1b1630;
  }
  * { margin: 0; padding: 0; box-sizing: border-box; }
  html, body { width: 1200px; height: 1000px; overflow: hidden; }
  body { font-family: 'Jost', sans-serif; color: var(--ink); background: var(--white); position: relative; }

  .site-header { position: absolute; top: 0; left: 0; width: 1200px; height: 103px; background: var(--white); z-index: 3; }
  .brand { position: absolute; left: 19px; top: 36px; display: flex; align-items: center; gap: 8px; font-weight: 400; font-size: 13px; letter-spacing: 2px; color: var(--ink); text-transform: uppercase; line-height: 1.15; }
  .brand-mark { width: 12px; height: 12px; background: var(--ink); flex: none; }
  .main-nav a { position: absolute; top: 60px; font-weight: 300; font-size: 15.5px; color: var(--ink); text-decoration: none; text-transform: uppercase; white-space: nowrap; }
  .nav-collections { left: 169px; }
  .nav-fine { left: 321px; }
  .nav-world { left: 487px; }
  .nav-bar { left: 753px; }
  .nav-blog { left: 884px; }
  .nav-events { left: 977px; }
  .header-tools { position: absolute; right: 31px; top: 21px; display: flex; gap: 16px; align-items: center; }

  .dropdown { position: absolute; left: 169px; top: 103px; width: 236px; height: 212px; background: var(--menu-bg); padding-top: 20px; z-index: 3; list-style: none; }
  .dropdown li { height: 37px; margin-bottom: 3px; padding-left: 21px; line-height: 37px; font-size: 16px; font-weight: 300; text-transform: uppercase; letter-spacing: 0.5px; white-space: nowrap; }
  .dropdown li.active { background: var(--menu-active); }

  .hero { position: absolute; top: 103px; left: 0; width: 1200px; height: 897px; overflow: hidden;
    background:
      radial-gradient(ellipse 520px 300px at 1080px 820px, var(--deep), transparent 80%),
      radial-gradient(ellipse 360px 220px at 1180px 60px, var(--skin), transparent 80%),
      radial-gradient(ellipse 420px 170px at 880px 120px, var(--teal-light), transparent 75%),
      linear-gradient(172deg, var(--teal) 0%, var(--teal) 26%, transparent 34%) 600px 0 / 600px 320px no-repeat,
      radial-gradient(ellipse 260px 180px at 90px 120px, var(--lace), transparent 80%),
      radial-gradient(ellipse 380px 240px at 380px 790px, var(--lace), transparent 80%),
      radial-gradient(ellipse 170px 260px at 60px 800px, var(--pearl-grey), transparent 80%),
      radial-gradient(ellipse 560px 380px at 780px 520px, var(--skin), transparent 80%),
      radial-gradient(ellipse 420px 360px at 260px 420px, var(--skin-soft), transparent 85%),
      linear-gradient(165deg, #e6c7bd 0%, #c99c94 45%, #6d5a6c 80%, var(--deep) 100%); }
  .hero-caption { position: absolute; bottom: 42px; left: 0; width: 1200px; text-align: center; color: var(--white); font-size: 16px; font-weight: 300; letter-spacing: 11px; text-transform: uppercase; }
  .hero-dot { position: absolute; left: 596px; bottom: 19px; }
</style>
</head>
<body>
  <header class="site-header">
    <div class="brand"><span class="brand-mark"></span><span>Keli<br>Dunmore</span></div>
    <nav class="main-nav">
      <a class="nav-collections" href="#">Collections</a>
      <a class="nav-fine" href="#">Fine Jewellery</a>
      <a class="nav-world" href="#">The World of Keli Dunmore</a>
      <a class="nav-bar" href="#">Pearl Bar</a>
      <a class="nav-blog" href="#">Blog</a>
      <a class="nav-events" href="#">Events</a>
    </nav>
    <div class="header-tools">
      <svg width="26" height="26" viewBox="0 0 26 26" fill="none" stroke="#333" stroke-width="1.6"><circle cx="10.5" cy="10.5" r="8.5"/><line x1="17" y1="17" x2="25" y2="25"/></svg>
      <svg width="20" height="26" viewBox="0 0 20 26" fill="none" stroke="#333" stroke-width="1.6"><path d="M10 25 C4 16 2 12 2 9 a8 8 0 0 1 16 0 c0 3 -2 7 -8 16z"/><circle cx="10" cy="9" r="3"/></svg>
      <svg width="22" height="26" viewBox="0 0 22 26" fill="none" stroke="#333" stroke-width="1.6"><rect x="2" y="7" width="18" height="18"/><path d="M7 7 V5 a4 4 0 0 1 8 0 V7"/><text x="11" y="21" font-family="Jost, sans-serif" font-size="12" text-anchor="middle" fill="#333" stroke="none">0</text></svg>
    </div>
  </header>

  <ul class="dropdown">
    <li>Alora</li>
    <li class="active">Strands of Grace</li>
    <li>Lyra</li>
    <li>Noa</li>
  </ul>

  <section class="hero" role="img" aria-label="Photograph of a woman lying on white lace over blue water, a hand fastening a long strand of grey and silver pearls around her neck">
    <p class="hero-caption">Keli Dunmore</p>
    <svg class="hero-dot" width="9" height="9" viewBox="0 0 9 9"><circle cx="4.5" cy="4.5" r="4.5" fill="#fff"/><path d="M4.5 0 A4.5 4.5 0 0 1 4.5 9z" fill="#1b1630" opacity="0.6"/></svg>
  </section>
</body>
</html>
```